Brin-well Tide Port Custom Brokers Limited

Name: Loranda Pascoe
Title: Customs Broker
Address: Shop 9 Fernvale Commercial Complex
227-229 Marrow Lane
Kingston 8
Telephone: (876)
Email: tideportbrin@quillmail.example

```html
<!DOCTYPE html>
<html lang="en">
<head>
<meta charset="utf-8">
<title>Brin-well Tide Port Custom Brokers Limited — Business Card</title>
<link rel="stylesheet" href="https://fonts.googleapis.com/css2?family=Source+Sans+3:wght@400;600;700&display=swap">
<style>
  :root {
    --page-bg: #e4e4e4;
    --navy: #102c52;
    --gold: #e6a521;
    --grey: #b3b3b5;
    --card-light: #f4f4f4;
    --ink: #2b2b2b;
    --muted: #9a9a9a;
  }
  * { margin: 0; padding: 0; box-sizing: border-box; }
  html, body {
    width: 1200px; height: 960px; overflow: hidden;
    background: var(--page-bg);
    font-family: "Source Sans 3", "Source Sans Pro", sans-serif;
  }
  .card {
    position: absolute; left: 317px; width: 568px; height: 325px;
    overflow: hidden;
  }
  .card--front { top: 134px; background: var(--navy); }
  .card--back { top: 508px; background: var(--card-light); }

  .front-brand {
    position: absolute; inset: 0;
    display: flex; flex-direction: column; align-items: center; justify-content: center;
    gap: 14px; color: #ffffff; font-weight: 600;
  }
  .front-brand__mark {
    width: 64px; height: 64px; border-radius: 50%; background: #ffffff;
  }
  .front-brand__name { font-size: 31px; letter-spacing: 1px; text-transform: uppercase; line-height: 1; }
  .front-brand__sub { font-size: 19px; letter-spacing: 4px; line-height: 1; }

  .back-brand {
    position: absolute; left: 38px; top: 38px;
    color: var(--navy); font-weight: 600; line-height: 1;
  }
  .back-brand__name { font-size: 24px; letter-spacing: 0.6px; text-transform: uppercase; }
  .back-brand__sub { font-size: 14px; letter-spacing: 3.4px; margin-top: 4px; padding-left: 21px; }

  .contact { position: absolute; left: 39px; top: 121px; color: var(--ink); }
  .contact__name { font-size: 19px; font-weight: 700; color: var(--navy); line-height: 1.1; }
  .contact__title { font-size: 14px; color: var(--gold); margin-top: 2px; }
  .contact__address { font-size: 15px; line-height: 19px; margin-top: 26px; }
  .contact__lines { list-style: none; font-size: 15px; line-height: 20px; margin-top: 7px; }
  .contact__lines li { display: flex; align-items: center; gap: 6px; }
  .contact__icon { width: 13px; height: 13px; flex: none; }

  .back-decor { position: absolute; inset: 0; }
</style>
</head>
<body>
  <section class="card card--front" aria-label="Card front">
    <div class="front-brand">
      <span class="front-brand__mark" aria-hidden="true"></span>
      <span class="front-brand__name">Brin-well Tide Port</span>
      <span class="front-brand__sub">Custom Brokers Ltd.</span>
    </div>
  </section>

  <section class="card card--back" aria-label="Card back">
    <svg class="back-decor" width="568" height="325" viewBox="0 0 568 325" aria-hidden="true">
      <path d="M520 0 L568 0 L568 290 L548 300 C555 200 555 90 520 0 Z" fill="var(--grey)"/>
      <path d="M498 0 L522 0 C552 70 552 160 520 240 C536 150 532 70 498 0 Z" fill="var(--gold)"/>
      <path d="M390 325 L568 268 L568 325 Z" fill="var(--grey)"/>
      <circle cx="520" cy="190" r="112" fill="var(--navy)"/>
    </svg>

    <div class="back-brand">
      <div class="back-brand__name">Brin-well Tide Port</div>
      <div class="back-brand__sub">Custom Brokers Ltd.</div>
    </div>

    <div class="contact">
      <div class="contact__name">Loranda Pascoe</div>
      <div class="contact__title">Customs Broker</div>
      <div class="contact__address">
        Shop 9 Fernvale Commercial Complex<br>
        227-229 Marrow Lane<br>
        Kingston 8
      </div>
      <ul class="contact__lines">
        <li>
          <svg class="contact__icon" viewBox="0 0 16 16" aria-hidden="true"><path fill="var(--gold)" d="M3.6 1.2l2.3 2.6c.4.4.4 1 0 1.4L4.7 6.5c.9 1.9 2.4 3.4 4.3 4.3l1.3-1.2c.4-.4 1-.4 1.4 0l2.6 2.3c.4.4.4 1 0 1.4l-1.2 1.3c-.6.6-1.5.8-2.3.5C6.3 13.6 2.4 9.7.9 5.2.6 4.4.8 3.5 1.4 2.9z"/></svg>
          <span>(876) 555-0142</span>
        </li>
        <li>
          <svg class="contact__icon" viewBox="0 0 16 16" aria-hidden="true"><rect x="1" y="3" width="14" height="10" fill="none" stroke="var(--gold)" stroke-width="1.6"/><path d="M1.5 3.5 8 9l6.5-5.5" fill="none" stroke="var(--gold)" stroke-width="1.6"/></svg>
          <span>tideportbrin@quillmail.example</span>
        </li>
      </ul>
    </div>
  </section>
</body>
</html>
```